Hearing Assessments & Hearing Aids

I need a business card design for my new business called 'Meridale Hearing Aids & Audiometry. I do hearing assessments for adults and children. I also fit hearing aids to hearing impaired people. I would also like to incorporate in my business card Aboriginal designs and colours with a picture of an ear which represents my hearing business as well as my Aboriginal culture.

I would also like my profession added to the business card. I am an Audioetrist.

Target Market(s)

My target customers are everyone concerned with theri hearing and for those who require hearing aids

Industry/Entity Type

Business

Contact Information for Business Card

Meridale Hearing Aids & Audiometry
Tom Harcastle
0432 519 604

Requirements
Must have
• Meridale Hearing Aids & Audiometry
Tom HArcastle
Mobile: 0432 519 604
Email: tomharcastle07@quellnet.com

Audiometrist

```html
<!DOCTYPE html>
<html lang="en">
<head>
<meta charset="utf-8">
<title>Meridale Hearing Aids &amp; Audiometry – Business Card</title>
<link rel="stylesheet" href="https://fonts.googleapis.com/css2?family=Ubuntu:wght@400;500;700&display=swap">
<style>
  :root {
    --backdrop: #e4e1df;
    --card: #fbfbfa;
    --ink: #1c1c1c;
    --accent: #c8141e;
    --divider: #2a2a2a;
    --earth-red: #c92a1f;
    --earth-orange: #e07a2a;
    --earth-brown: #5a2a1c;
    --earth-navy: #23306e;
    --earth-teal: #2a7f8c;
  }
  * { box-sizing: border-box; margin: 0; padding: 0; }
  html, body {
    width: 1200px; height: 840px; overflow: hidden;
    background: var(--backdrop);
    font-family: "Ubuntu", sans-serif;
    color: var(--ink);
  }
  .canvas { position: relative; width: 1200px; height: 840px; }
  .card {
    position: absolute; top: 286px;
    width: 467px; height: 267px;
    background: var(--card);
  }
  .card--front { left: 75px; }
  .card--back { left: 671px; }

  .ear-artwork {
    position: absolute;
    border-radius: 50% 50% 46% 54% / 44% 48% 52% 56%;
    background: radial-gradient(circle at 45% 35%, var(--earth-teal) 0%, var(--earth-orange) 30%, var(--earth-red) 55%, var(--earth-navy) 75%, var(--earth-brown) 100%);
  }
  .card--front .ear-artwork { left: 93px; top: 72px; width: 64px; height: 97px; }
  .card--back .ear-artwork { left: 180px; top: 62px; width: 110px; height: 156px; }

  .company-name {
    position: absolute; left: 10px; width: 240px; top: 181px;
    text-align: center;
    font-weight: 700; font-size: 9.6px; letter-spacing: 0.1px;
    text-transform: uppercase;
  }
  .divider {
    position: absolute; left: 248px; top: 85px;
    width: 1.5px; height: 93px; background: var(--divider);
  }
  .person { position: absolute; left: 283px; top: 66px; }
  .person__name { font-size: 16px; font-weight: 500; line-height: 20px; }
  .person__role { font-size: 13px; line-height: 18px; }

  .contact-list {
    position: absolute; left: 262px; top: 122px;
    list-style: none; font-size: 13px; line-height: 18.5px;
  }
  .contact-list li { display: flex; align-items: center; }
  .contact-list svg { width: 10px; height: 10px; margin-right: 11px; flex: none; }
</style>
</head>
<body>
<main class="canvas">
  <section class="card card--front">
    <div class="ear-artwork" role="img" aria-label="Dot-painted ear artwork in Aboriginal colours"></div>
    <p class="company-name">Meridale Hearing Aids &amp; Audiometry</p>
    <div class="divider"></div>
    <div class="person">
      <h1 class="person__name">Tom HArcastle</h1>
      <p class="person__role">Audiometrist</p>
    </div>
    <ul class="contact-list">
      <li>
        <svg viewBox="0 0 10 10" aria-hidden="true"><rect x="2.5" y="0.5" width="5" height="9" rx="1" fill="none" stroke="var(--accent)" stroke-width="1.2"/><rect x="4.2" y="7.4" width="1.6" height="0.9" fill="var(--accent)"/></svg>
        0432 519 604
      </li>
      <li>
        <svg viewBox="0 0 10 10" aria-hidden="true"><circle cx="5" cy="5" r="4" fill="var(--accent)"/></svg>
        @TomHarcastle
      </li>
      <li>
        <svg viewBox="0 0 10 10" aria-hidden="true"><rect x="0.5" y="2" width="9" height="6.5" fill="var(--accent)"/><path d="M0.8 2.3 L5 5.6 L9.2 2.3" fill="none" stroke="var(--card)" stroke-width="0.9"/></svg>
        tom.harcastle@mhaa.com
      </li>
      <li>
        <svg viewBox="0 0 10 10" aria-hidden="true"><circle cx="5" cy="5" r="4.2" fill="var(--accent)"/><path d="M1 5 H9 M5 0.8 C3 3 3 7 5 9.2 M5 0.8 C7 3 7 7 5 9.2" fill="none" stroke="var(--card)" stroke-width="0.7"/></svg>
        www.yourwebsite.com
      </li>
    </ul>
  </section>

  <section class="card card--back">
    <div class="ear-artwork" role="img" aria-label="Large dot-painted ear artwork in Aboriginal colours"></div>
  </section>
</main>
</body>
</html>
```